beauty salon

providing waxing services from a home base this must include which I will provide a price list and an address

Industry/Entity Type

Beauty Salon

Font styles to use
Script

Colors

Designer to choose colors to be used in the design.

```html
<!DOCTYPE html>
<html lang="en">
<head>
<meta charset="utf-8">
<title>Amara's Haven Salon – Waxing Price List</title>
<link rel="stylesheet" href="https://fonts.googleapis.com/css2?family=Arimo:wght@400;700&family=Signika:wght@400;600&display=swap">
<style>
  :root {
    --magenta: #b81c8e;
    --plum: #6b2a7c;
    --orchid: #9a2f90;
    --emerald: #13ae7c;
    --white: #ffffff;
    --ink: #3d3d3d;
    --backdrop: #ececec;
    --photo-skin: #e8c3a6;
    --photo-pale: #f1e6df;
  }
  * { box-sizing: border-box; margin: 0; padding: 0; }
  html, body { width: 1200px; height: 1000px; overflow: hidden; background: var(--backdrop); }
  body { position: relative; font-family: "Arimo", Arial, sans-serif; }

  .flyer {
    position: absolute; left: 252px; top: 50px; width: 696px; height: 900px; overflow: hidden;
    background: linear-gradient(100deg, var(--magenta) 0%, #a42190 55%, var(--plum) 100%);
    color: var(--white);
  }

  .header-petals {
    position: absolute; left: 140px; top: 15px; width: 416px; height: 260px;
    border-radius: 50% 50% 40% 40%;
    background: radial-gradient(ellipse at 50% 70%, rgba(255,255,255,.35), rgba(255,255,255,0) 70%);
  }
  .header-card {
    position: absolute; left: 180px; top: 122px; width: 336px; height: 172px;
    background: var(--white); border-radius: 50%;
    text-align: center; color: var(--ink);
  }
  .brand { display: flex; align-items: center; justify-content: center; gap: 8px; margin-top: 38px; }
  .brand-dot { width: 12px; height: 12px; border-radius: 50%; background: var(--emerald); }
  .brand-name { font-family: "Signika", "Trebuchet MS", sans-serif; font-weight: 400; font-size: 22px; color: var(--orchid); }
  .therapist { font-size: 13.5px; line-height: 17px; margin-top: 8px; }

  .headline {
    position: absolute; left: 0; width: 100%; top: 308px; text-align: center;
    font-weight: 700; font-size: 22.5px; letter-spacing: -.2px;
  }

  .photo {
    position: absolute; top: 346px; width: 206px; height: 137px;
    border: 4px solid var(--white); border-radius: 9px;
    box-shadow: 0 2px 5px rgba(0,0,0,.25);
  }
  .photo--legs { left: 33px; background: linear-gradient(120deg, var(--white) 30%, var(--photo-skin) 60%, var(--white) 85%); }
  .photo--chest { left: 246px; background: linear-gradient(180deg, var(--white) 15%, var(--photo-skin) 45%, #d9a47f 100%); }
  .photo--eyes { left: 459px; background: linear-gradient(180deg, var(--photo-pale), #e2c3ae 55%, var(--photo-pale)); }

  .connector { position: absolute; left: 0; top: 480px; width: 696px; height: 60px; }

  .price-tag {
    position: absolute; left: 280px; top: 501px; width: 136px; height: 31px;
    background: var(--white); border-radius: 4px; color: var(--orchid);
    font-weight: 700; font-size: 20px; text-align: center; line-height: 31px;
    box-shadow: 0 2px 4px rgba(0,0,0,.2);
  }

  .price-column { position: absolute; top: 556px; width: 162px; font-size: 13px; }
  .price-column--lady { left: 42px; }
  .price-column--men { left: 268px; }
  .price-column--eye { left: 494px; }
  .column-title {
    border-top: 2px solid var(--white); border-bottom: 2px solid var(--white);
    text-align: center; font-weight: 700; font-size: 16px; height: 31px; line-height: 29px;
    margin-bottom: 12px;
  }
  .price-row { display: flex; align-items: baseline; height: 16.5px; }
  .price-row .leader { flex: 1; border-bottom: 1px dotted rgba(255,255,255,.85); margin: 0 2px; transform: translateY(-3px); }
  .price-row .amount { font-weight: 700; }

  .offer-badge {
    position: absolute; left: 473px; top: 675px; width: 190px; height: 190px; border-radius: 50%;
    background: var(--emerald); box-shadow: 0 6px 10px rgba(0,0,0,.3);
    text-align: center;
  }
  .offer-badge::before {
    content: ""; position: absolute; inset: 6px; border: 2px solid var(--white); border-radius: 50%;
  }
  .offer-value { font-size: 48px; font-weight: 700; margin-top: 38px; line-height: 52px; }
  .offer-text { font-size: 18px; line-height: 23px; }

  .hours-badge {
    position: absolute; left: 258px; top: 772px; width: 222px; height: 222px; border-radius: 50%;
    background: var(--white); color: #111; text-align: center; font-size: 13.5px; line-height: 17px;
    box-shadow: 0 0 6px rgba(0,0,0,.25);
  }
  .hours-title { color: var(--emerald); font-weight: 700; font-size: 17px; margin: 36px 0 3px; }

  .address-bar {
    position: absolute; left: 0; top: 860px; width: 260px; height: 25px;
    background: var(--emerald); font-size: 14px; line-height: 25px; padding-left: 37px;
  }
</style>
</head>
<body>
  <main class="flyer">
    <div class="header-petals" role="img" aria-label="White lotus flower outline framing the salon header"></div>
    <header class="header-card">
      <div class="brand"><span class="brand-dot"></span><span class="brand-name">Amara's Haven Salon</span></div>
      <p class="therapist">Beauty Therapist: Amara<br>Diploma of Beauty Therapy at Renwick College<br>mobile: 0400 555 018</p>
    </header>

    <h1 class="headline">PROVIDING WAXING SERVICES FROM A HOME BASE</h1>

    <div class="photo photo--legs" role="img" aria-label="Photo of smooth waxed legs"></div>
    <div class="photo photo--chest" role="img" aria-label="Photo of a man's chest half waxed"></div>
    <div class="photo photo--eyes" role="img" aria-label="Close-up photo of eyes and brows"></div>

    <svg class="connector" viewBox="0 0 696 60" aria-hidden="true">
      <path d="M126 10 Q150 36 190 36 L280 36 M416 36 L506 36 Q546 36 570 10" fill="none" stroke="#fff" stroke-width="2.5" stroke-dasharray="10 8"/>
    </svg>
    <div class="price-tag">PRICE LIST</div>

    <section class="price-column price-column--lady">
      <h2 class="column-title">LADY'S WAXING</h2>
      <div class="price-row"><span>Eyebrow</span><span class="leader"></span><span class="amount">$8</span></div>
      <div class="price-row"><span>Upper lip</span><span class="leader"></span><span class="amount">$8</span></div>
      <div class="price-row"><span>Chin</span><span class="leader"></span><span class="amount">$8</span></div>
      <div class="price-row"><span>Face wax</span><span class="leader"></span><span class="amount">$25</span></div>
      <div class="price-row"><span>Bikini line</span><span class="leader"></span><span class="amount">$15</span></div>
      <div class="price-row"><span>G string</span><span class="leader"></span><span class="amount">$20</span></div>
      <div class="price-row"><span>½ Brazilian</span><span class="leader"></span><span class="amount">$30</span></div>
      <div class="price-row"><span>Full Brazilian</span><span class="leader"></span><span class="amount">$40</span></div>
      <div class="price-row"><span>Half arm</span><span class="leader"></span><span class="amount">$20</span></div>
      <div class="price-row"><span>Upper half arm</span><span class="leader"></span><span class="amount">$20</span></div>
      <div class="price-row"><span>Full arm</span><span class="leader"></span><span class="amount">$25</span></div>
      <div class="price-row"><span>Half leg</span><span class="leader"></span><span class="amount">$15</span></div>
      <div class="price-row"><span>Upper leg</span><span class="leader"></span><span class="amount">$20</span></div>
      <div class="price-row"><span>¾ Leg</span><span class="leader"></span><span class="amount">$25</span></div>
      <div class="price-row"><span>Full leg</span><span class="leader"></span><span class="amount">$35</span></div>
    </section>

    <section class="price-column price-column--men">
      <h2 class="column-title">MEN'S WAXING</h2>
      <div class="price-row"><span>Eyebrow</span><span class="leader"></span><span class="amount">$10</span></div>
      <div class="price-row"><span>Half arm</span><span class="leader"></span><span class="amount">$20</span></div>
      <div class="price-row"><span>Upper half arm</span><span class="leader"></span><span class="amount">$25</span></div>
      <div class="price-row"><span>Full arm</span><span class="leader"></span><span class="amount">$30</span></div>
      <div class="price-row"><span>Half leg</span><span class="leader"></span><span class="amount">$25</span></div>
      <div class="price-row"><span>Full leg</span><span class="leader"></span><span class="amount">$45</span></div>
      <div class="price-row"><span>Chest wax</span><span class="leader"></span><span class="amount">$40</span></div>
      <div class="price-row"><span>Back wax</span><span class="leader"></span><span class="amount">$35</span></div>
    </section>

    <section class="price-column price-column--eye">
      <h2 class="column-title">EYE ENHANCEMENT</h2>
      <div class="price-row"><span>Eyebrow tint</span><span class="leader"></span><span class="amount">$12</span></div>
      <div class="price-row"><span>Eyelash tint</span><span class="leader"></span><span class="amount">$15</span></div>
    </section>

    <div class="offer-badge">
      <p class="offer-value">10%</p>
      <p class="offer-text">discount on<br>first treatment.</p>
    </div>

    <div class="address-bar">12 Finch Lane, Eastwood Vale</div>

    <div class="hours-badge">
      <p class="hours-title">Now Open:</p>
      <p>Wednesday 10am – 4pm<br>Fridays 10am-7pm<br>Saturday 10am -4pm</p>
    </div>
  </main>
</body>
</html>
```